Managed Service Provider VOIP Flyer

Looking for a one page US letter size single or double sided brochure to offer cloud hosted VoIP Phone system and unified communications. We have partnered with a VoIP Phone system company and want to sell their services but we don't want their name to be shown on the brochure because customers might call them directly. The company name is Quorvel (www.quorvel-example.com) and our company name is Lumen By Harlow, LLC and our voice product is called Clearly Talk. I have also uploaded my company's logo that you should show on the brochure and use that coloring. For more details about the product, you can visit their website mentioned above. Also I am looking for something very similar to this project and many of the technical details are the same https://flyer.contestpad-example.com/contest/5817264

I have also uploaded a PDF with my different package levels and some of the included features. Depending on the design we may or may not want the package levels on this flyer.

Target Market(s)

Small and medium Businesses

Industry/Entity Type

Voip

Requirements
Must have
• Feature and benefits information of Managed VOICE. Use my logo and coloring from my logo. Include our website, email, phone and possibly facebook if it makes sense/looks good.

www.lumenbyharlow-example.com
415.836.0.917
sales@lumenbyharlow-example.com
www.socialsite-example.com/lumenbyharlow
Nice to have
• Would like to show how the service is simple and reliable and available for any business size

```html
<!DOCTYPE html>
<html lang="en">
<head>
<meta charset="utf-8">
<title>Lumen By Harlow – Cloud Phone System Flyer</title>
<link href="https://fonts.googleapis.com/css2?family=Source+Sans+3:wght@400;600;700&family=Varela+Round&display=swap" rel="stylesheet">
<style>
  :root{
    --navy:#0f1b3d;
    --navy-2:#16254f;
    --red:#c4241c;
    --red-2:#a91d17;
    --ink:#2b2b2b;
    --muted:#555;
    --bg:#8e8e8e;
  }
  *{box-sizing:border-box;margin:0;padding:0}
  html,body{width:1200px;height:838px;overflow:hidden;background:var(--bg);font-family:"Source Sans 3",sans-serif;font-weight:400;color:var(--ink)}
  h1,h2,p,li,th,td{font-weight:400}
  .page{position:absolute;top:87px;width:487px;height:632px;background:#fff;overflow:hidden;box-shadow:0 4px 14px rgba(0,0,0,.35)}
  .page--front{left:91px}
  .page--back{left:638px}

  /* front header */
  .brand{position:absolute;top:0;left:0;width:100%;height:72px;display:flex;align-items:center;justify-content:center;gap:10px}
  .brand__mark{width:20px;height:20px;border-radius:50%;background:var(--red)}
  .brand__name{font-weight:700;font-size:21px;color:var(--navy);letter-spacing:.3px}

  .hero{position:absolute;top:72px;left:0;width:100%;height:236px;background:var(--navy);overflow:hidden}
  .hero__photo{position:absolute;left:215px;top:0;width:272px;height:236px;background:radial-gradient(circle at 55% 55%,#3a8fd0 0%,#1b4f86 30%,#0f2a55 60%,#0b1836 100%)}
  .hero__title{position:absolute;left:20px;top:20px;font-family:"Varela Round",sans-serif;font-weight:400;font-size:21px;line-height:25px;color:#fff}
  .hero__title em{font-style:normal;color:#d8322a}
  .hero__copy{position:absolute;left:20px;width:195px;font-size:6.2px;line-height:7.6px;color:#e8ecf5;text-align:justify}
  .notch-down{position:absolute;width:0;height:0;border-left:11px solid transparent;border-right:11px solid transparent}

  .benefits__title{position:absolute;top:323px;left:0;width:100%;text-align:center;font-size:19.5px;font-weight:600;color:var(--navy);letter-spacing:.3px}
  .benefits__title span{color:var(--red)}
  .benefit{position:absolute;left:0;width:487px}
  .benefit__band{position:absolute;left:0;top:14px;width:44px;height:16px;background:var(--navy)}
  .benefit__hex{position:absolute;left:30px;top:-3px}
  .benefit__body{position:absolute;left:80px;top:0;width:386px}
  .benefit__head{font-size:7.6px;font-weight:700;color:var(--red);line-height:9.5px}
  .benefit__text{font-size:6.7px;line-height:8.1px;color:var(--muted);text-align:justify}

  /* footer */
  .footer{position:absolute;left:0;bottom:0;width:100%;height:46px;background:var(--navy)}
  .footer__phone{position:absolute;left:22px;top:12px;display:flex;align-items:center;gap:6px;color:#fff;font-size:18px;white-space:nowrap}
  .footer__red{position:absolute;right:0;bottom:0;width:300px;height:38px;background:var(--red-2);clip-path:polygon(0 0,100% 0,100% 100%,6% 100%)}
  .footer__web{position:absolute;right:20px;top:6px;color:#fff;font-size:8.8px;text-align:right;line-height:12px;white-space:nowrap}
  .footer__loc{font-size:7px;line-height:10px;color:#fff;display:block}

  /* back */
  .back__title{position:absolute;top:26px;left:0;width:100%;text-align:center;font-size:17px;font-weight:600;color:var(--navy);white-space:nowrap}
  .back__title span{color:var(--red)}
  .timeline{position:absolute;top:84px;left:36px;width:420px;height:1px;background:#888}
  .service{position:absolute;top:60px;width:100px;text-align:center}
  .service__hex{display:block;margin:0 auto}
  .service__name{margin-top:6px;font-size:6.6px;font-weight:700;line-height:8px;text-transform:uppercase}
  .service__name--red{color:var(--red)}
  .service__name--navy{color:var(--navy)}
  .service__desc{margin:4px auto 0;width:86px;font-size:5.7px;line-height:7.2px;color:var(--muted)}

  .features{position:absolute;top:191px;left:0;width:100%;height:187px;background:linear-gradient(90deg,var(--navy) 0%,var(--navy-2) 50%,var(--navy) 100%)}
  .features__title{position:absolute;top:20px;width:100%;text-align:center;color:#fff;font-size:11px}
  .features__title span{color:#e0392f}
  .features__col{position:absolute;top:44px;list-style:none}
  .features__col li{font-size:8px;line-height:15.3px;color:#fff;display:flex;align-items:center;gap:5px;white-space:nowrap}
  .features__col li::before{content:"";width:5px;height:5px;border:1px solid #d8322a;border-radius:50%}

  .plans{position:absolute;top:378px;left:0;width:100%;height:208px}
  .plans__bg{position:absolute;inset:0;background:linear-gradient(180deg,#e9e9ec 0%,#f7f7f7 60%,#fff 100%)}
  .plans__table{position:absolute;left:21px;top:25px;width:441px;border-collapse:collapse;table-layout:fixed}
  .plans__table th{height:30px;color:#fff;vertical-align:middle}
  .plans__table .th-label{background:var(--navy);text-align:left;padding-left:34px;font-size:13px;width:173px}
  .plans__table .th-plan{background:var(--red);font-size:7.6px;font-weight:600;line-height:8px;border-right:1px solid #fff}
  .plans__table .th-plan small{display:block;font-size:5px;font-weight:400;margin-top:2px}
  .plans__table .th-blank{background:#fff;border:1px solid #ccc;border-bottom:none}
  .plans__table td{height:31px;font-size:7.5px;text-align:center;border-bottom:1px solid #ddd;background:#fafafa;color:#444;position:relative}
  .plans__table td.label{text-align:left;padding-left:34px;background:#fff;color:#333}
  .plans__table td.label svg{position:absolute;left:12px;top:11px}
  .plans__table tr.price td{font-weight:700;color:#111;background:#fff}
  .plans__table tr.price td.val::before{content:"";position:absolute;left:0;top:10px;border-top:5px solid transparent;border-bottom:5px solid transparent;border-left:6px solid var(--red)}
  .plans__rule{position:absolute;left:21px;top:180px;width:441px;height:4px;background:linear-gradient(90deg,var(--navy) 0 39%,var(--red) 39% 100%)}
</style>
</head>
<body>

<section class="page page--front">
  <header class="brand">
    <span class="brand__mark"></span>
    <span class="brand__name">Lumen By Harlow</span>
  </header>

  <div class="hero">
    <div class="hero__photo" role="img" aria-label="Hand holding a glowing digital cube with a padlock, surrounded by cloud, phone, email and device icons"></div>
    <h1 class="hero__title"><em>A Cloud-Based</em><br>Phone System<br>For Businesses</h1>
    <p class="hero__copy" style="top:116px">We can help you grow your business by modernizing your company's phone system and making it easy to use, manage, and track directly from the cloud</p>
    <p class="hero__copy" style="top:154px">Our cloud business phone system adapts to your economic challenges and brings flexibility and adaptability to your business communications whilst considerably reducing costs compared to traditional phone systems. We take great pride in continually improving our platform as well as developing new features and services that in turn increase our customers' productivity.</p>
  </div>
  <div class="notch-down" style="top:72px;left:234px;border-top:10px solid #fff"></div>
  <div class="notch-down" style="top:308px;left:234px;border-top:10px solid var(--navy)"></div>

  <h2 class="benefits__title"><span>BENEFITS</span> OF CLOUD-BASED PHONE SYSTEM</h2>

  <div class="benefit" style="top:367px">
    <div class="benefit__band"></div>
    <svg class="benefit__hex" width="44" height="50" viewBox="0 0 44 50"><polygon points="22,1 43,13 43,37 22,49 1,37 1,13" fill="#fff" stroke="#c4241c" stroke-width="1.5"/><polygon points="22,5 39,15 39,35 22,45 5,35 5,15" fill="#0f1b3d"/><rect x="17" y="16" width="10" height="18" rx="2" fill="none" stroke="#fff" stroke-width="1.5"/><circle cx="22" cy="31" r="1" fill="#fff"/></svg>
    <div class="benefit__body">
      <p class="benefit__head">BECOME MOBILE</p>
      <p class="benefit__text">From our cloud-based telephony and its unified communications system emerges the concept of mobility. Make calls using your office phone, computer, or mobile phone, and chat with your colleagues and customers from numerous locations.<br>Enjoy centralized communications and simplified management.</p>
    </div>
  </div>
  <div class="benefit" style="top:420px">
    <div class="benefit__band"></div>
    <svg class="benefit__hex" width="44" height="50" viewBox="0 0 44 50"><polygon points="22,1 43,13 43,37 22,49 1,37 1,13" fill="#fff" stroke="#c4241c" stroke-width="1.5"/><polygon points="22,5 39,15 39,35 22,45 5,35 5,15" fill="#0f1b3d"/><circle cx="19" cy="18" r="4" fill="#fff"/><ellipse cx="24" cy="28" rx="9" ry="6" fill="#fff"/></svg>
    <div class="benefit__body">
      <p class="benefit__head">SAVE COSTS</p>
      <p class="benefit__text">The fixed and operating costs of your business communications are substantially reduced, and we take care of installing, configuring, and managing your phone system. Call us today for free consultation.</p>
    </div>
  </div>
  <div class="benefit" style="top:468px">
    <div class="benefit__band"></div>
    <svg class="benefit__hex" width="44" height="50" viewBox="0 0 44 50"><polygon points="22,1 43,13 43,37 22,49 1,37 1,13" fill="#fff" stroke="#c4241c" stroke-width="1.5"/><polygon points="22,5 39,15 39,35 22,45 5,35 5,15" fill="#0f1b3d"/><path d="M14 20 A10 10 0 0 0 26 34 Z" fill="#fff"/><line x1="20" y1="27" x2="29" y2="18" stroke="#fff" stroke-width="1.5"/><line x1="20" y1="30" x2="18" y2="36" stroke="#fff" stroke-width="1.5"/></svg>
    <div class="benefit__body">
      <p class="benefit__head">STAY ABREAST</p>
      <p class="benefit__text">Enjoy leading-edge telecommunications technology and its host of features that adapt to your needs, whatever the size of your business. These features are constantly upscaled and automatically updated. You will thus never have to operate an obsolete system.</p>
    </div>
  </div>
  <div class="benefit" style="top:521px">
    <div class="benefit__band"></div>
    <svg class="benefit__hex" width="44" height="50" viewBox="0 0 44 50"><polygon points="22,1 43,13 43,37 22,49 1,37 1,13" fill="#fff" stroke="#c4241c" stroke-width="1.5"/><polygon points="22,5 39,15 39,35 22,45 5,35 5,15" fill="#0f1b3d"/><path d="M14 30 a5 5 0 0 1 2-9 a7 7 0 0 1 13 1 a4 4 0 0 1 0 8 z" fill="#fff"/></svg>
    <div class="benefit__body">
      <p class="benefit__head">AVOID INCONVENIENCES</p>
      <p class="benefit__text">We take charge of the structure of your business phone system and remove the PBX (Private Branch Exchange) system to host it in its cloud database, thus saving you space, time, and costs. You are cleared of wire clutter and your business communications are streamlined, allowing you to work freely and efficiently. Also, this service includes an excellent recovery and business continuity plan that prevents unforeseen events, such as claims or system failures, from leading to data loss or suspension of business activities.</p>
    </div>
  </div>

  <footer class="footer">
    <div class="footer__phone">
      <svg width="20" height="20" viewBox="0 0 20 20"><rect x="6" y="1" width="11" height="18" rx="2" fill="none" stroke="#fff" stroke-width="1.6"/><path d="M2 7 q-1 4 1 9 l3 -1 v-7 z" fill="#fff"/></svg>
      <span>+1 (415) 836-0917</span>
    </div>
    <div class="footer__red">
      <p class="footer__web">www.lumenbyharlow-example.com | sales@lumenbyharlow-example.com<span class="footer__loc">Oregon, United States</span></p>
    </div>
  </footer>
</section>

<section class="page page--back">
  <h2 class="back__title"><span>A CLOUD-BASED PHONE SYSTEM</span> FOR BUSINESSES</h2>
  <div class="timeline"></div>

  <div class="service" style="left:41px">
    <svg class="service__hex" width="52" height="46" viewBox="0 0 52 46"><polygon points="13,1 39,1 51,23 39,45 13,45 1,23" fill="#fff" stroke="#c4241c" stroke-width="1.2"/><polygon points="15,5 37,5 47,23 37,41 15,41 5,23" fill="#c4241c"/><rect x="20" y="14" width="12" height="18" rx="2" fill="none" stroke="#fff" stroke-width="1.4"/><line x1="23" y1="19" x2="29" y2="19" stroke="#fff"/><line x1="23" y1="23" x2="29" y2="23" stroke="#fff"/><line x1="23" y1="27" x2="29" y2="27" stroke="#fff"/></svg>
    <p class="service__name service__name--red">Cloud Phone<br>System</p>
    <p class="service__desc">Your business phone system, now in the cloud. Access every feature from anywhere.</p>
  </div>
  <div class="service" style="left:138px">
    <svg class="service__hex" width="52" height="46" viewBox="0 0 52 46"><polygon points="13,1 39,1 51,23 39,45 13,45 1,23" fill="#fff" stroke="#0f1b3d" stroke-width="1.2"/><polygon points="15,5 37,5 47,23 37,41 15,41 5,23" fill="#0f1b3d"/><circle cx="26" cy="23" r="2.5" fill="#fff"/><g stroke="#fff" stroke-width="1"><line x1="26" y1="23" x2="19" y2="15"/><line x1="26" y1="23" x2="34" y2="16"/><line x1="26" y1="23" x2="18" y2="29"/><line x1="26" y1="23" x2="33" y2="31"/></g><g fill="#fff"><circle cx="19" cy="15" r="2"/><circle cx="34" cy="16" r="2"/><circle cx="18" cy="29" r="2"/><circle cx="33" cy="31" r="2"/></g></svg>
    <p class="service__name service__name--navy">Unified<br>Communications</p>
    <p class="service__desc">A powerful suite of communications and collaboration tools grouped under one platform.</p>
  </div>
  <div class="service" style="left:238px">
    <svg class="service__hex" width="52" height="46" viewBox="0 0 52 46"><polygon points="13,1 39,1 51,23 39,45 13,45 1,23" fill="#fff" stroke="#c4241c" stroke-width="1.2"/><polygon points="15,5 37,5 47,23 37,41 15,41 5,23" fill="#c4241c"/><circle cx="26" cy="19" r="5" fill="#fff"/><path d="M17 33 q9 -12 18 0 z" fill="#fff"/><path d="M20 19 a6 6 0 0 1 12 0" fill="none" stroke="#fff" stroke-width="1.2"/></svg>
    <p class="service__name service__name--red">Contact<br>Center</p>
    <p class="service__desc">Manage your different customer contact points from a unified, user-friendly web interface.</p>
  </div>
  <div class="service" style="left:336px">
    <svg class="service__hex" width="52" height="46" viewBox="0 0 52 46"><polygon points="13,1 39,1 51,23 39,45 13,45 1,23" fill="#fff" stroke="#0f1b3d" stroke-width="1.2"/><polygon points="15,5 37,5 47,23 37,41 15,41 5,23" fill="#0f1b3d"/><rect x="16" y="13" width="20" height="12" rx="1" fill="none" stroke="#fff" stroke-width="1.3"/><circle cx="26" cy="28" r="2" fill="#fff"/><path d="M22 34 q4 -5 8 0 z" fill="#fff"/></svg>
    <p class="service__name service__name--navy">Meet<br>Studio</p>
    <p class="service__desc">A flexible yet easy-to-use online administration portal to manage your business phone system.</p>
  </div>

  <div class="features">
    <p class="features__title">INCLUDED <span>FEATURES</span></p>
    <ul class="features__col" style="left:21px">
      <li>3-Way Calling</li><li>Call Logs</li><li>Caller ID and Caller Name Delivery</li><li>Call Waiting</li><li>Call Forward Always</li><li>Call Forward Busy</li><li>Call Forward No Answer</li><li>Call Forward Not Reachable</li>
    </ul>
    <ul class="features__col" style="left:196px">
      <li>Do Not Disturb</li><li>Extension Dialing</li><li>Last Number Redial</li><li>Simultaneous Ring</li><li>Sequential Ring</li><li>Speed Dial 100</li><li>Unified Messaging</li><li>Advanced Auto Attendant</li>
    </ul>
    <ul class="features__col" style="left:365px">
      <li>Call Recording</li><li>Toll-Free Numbers</li><li>Virtual Number</li><li>Auto Attendant</li><li>Company Main Number</li><li>Corporate Directory</li><li>Hunt Groups</li><li>Music on Hold</li>
    </ul>
  </div>
  <div class="notch-down" style="top:191px;left:232px;border-top:9px solid #fff"></div>

  <div class="plans">
    <div class="plans__bg" role="img" aria-label="Faded office photograph behind the pricing table"></div>
    <table class="plans__table">
      <tr>
        <th class="th-label">SERVICE PLANS</th>
        <th class="th-plan">PRIMER<small>(Location, not a user)</small></th>
        <th class="th-plan">STANDARD<small>(Basic user)</small></th>
        <th class="th-blank"></th>
      </tr>
      <tr class="price">
        <td class="label"><svg width="12" height="9" viewBox="0 0 12 9"><path d="M0 4.5h10M6.5 1l3.5 3.5L6.5 8" fill="none" stroke="#c4241c" stroke-width="1.4"/></svg>MONTHLY ACCOUNT PRICE</td>
        <td class="val">$20.00</td><td class="val">$30.00</td><td class="val">$35.00</td>
      </tr>
      <tr>
        <td class="label"><svg width="12" height="9" viewBox="0 0 12 9"><path d="M0 4.5h10M6.5 1l3.5 3.5L6.5 8" fill="none" stroke="#c4241c" stroke-width="1.4"/></svg>0 to 19 users</td>
        <td>$18.00</td><td>$20.00</td><td>$22.00</td>
      </tr>
      <tr>
        <td class="label"><svg width="12" height="9" viewBox="0 0 12 9"><path d="M0 4.5h10M6.5 1l3.5 3.5L6.5 8" fill="none" stroke="#c4241c" stroke-width="1.4"/></svg>20 to 49 users</td>
        <td>$15.00</td><td>$17.00</td><td>$16.00</td>
      </tr>
      <tr>
        <td class="label"><svg width="12" height="9" viewBox="0 0 12 9"><path d="M0 4.5h10M6.5 1l3.5 3.5L6.5 8" fill="none" stroke="#c4241c" stroke-width="1.4"/></svg>50to 99 users</td>
        <td>$12.00</td><td>$14.00</td><td>$16.00</td>
      </tr>
    </table>
    <div class="plans__rule"></div>
  </div>

  <footer class="footer">
    <div class="footer__phone">
      <svg width="20" height="20" viewBox="0 0 20 20"><rect x="6" y="1" width="11" height="18" rx="2" fill="none" stroke="#fff" stroke-width="1.6"/><path d="M2 7 q-1 4 1 9 l3 -1 v-7 z" fill="#fff"/></svg>
      <span>+1 (415) 836-0917</span>
    </div>
    <div class="footer__red">
      <p class="footer__web">www.lumenbyharlow-example.com | sales@lumenbyharlow-example.com<span class="footer__loc">Oregon, United States</span></p>
    </div>
  </footer>
</section>

</body>
</html>
```